Business card for Les Brisants-Corail campsite

HORIZONTAL / 85x55
OBJECTIVE
Create a modern, attractive and memorable business card for the Les Brisants-Corail campsite, located on the Île d'Oléron.
The map should make people want to discover the campsite and immediately convey its world: ocean, holidays, nature and conviviality.
VISUAL IDENTITY
The design must be in the same graphic style as our website:
www.lesbrisants-corail.fr
The site is the main reference for the visual atmosphere: colours, typography, shapes, photographs and general universe.
The map and the site must give the impression of belonging to a single brand identity.
A UNIVERSE TO TRANSMIT
• Île d'Oléron
• Atlantic Ocean
• Seaside
• Direct access to the beaches
• Vacation
• Nature
• Family-friendly and welcoming atmosphere
• Relaxation
DESIRED STYLE
Bright, warm, modern, nautical and natural.
We want a creation with a real personality, immediately recognizable, and not a generic camping business card.
FRONT
Prioritize visual impact with:
• Official logo Les Brisants-Corail
• Île d'Oléron
• A strong evocation of the ocean and holidays
• A short and memorable hook
The designer is free to propose their own hook.
BACK
The Coral Breakers
Villages 1 & 2
22 Rue des Mouettes
17310 Saint-Pierre-d'Oléron
France
Tel.: +33 5 47 12 38 04
www.lesbrisants-corail. fr
Possibility of discreet integration:
Direct access to the beaches
Mobile homes • Pitches • Accommodation
Le Varech Bar-Restaurant
FORMAT
Double-sided card: 85 × 55 mm.
Horizontal orientation
AVOID
• Overly institutional design
• Overloaded map
• Generic "camping" style
• Too many pictograms
• Accumulation of texts
• Modification or distortion of the official logo
• Graphic design unrelated to the website
CREATIVE FREEDOM
We are looking for an original proposal.
The designer can play with the graphic codes of the ocean, waves, sun, beach and Île d'Oléron, while remaining faithful to the visual identity of the site.
The card must be aesthetically pleasing and original enough to make people want to keep it.
The objective:
See the map → think about the ocean and holidays → remember Les Brisants-Corail → discover the campsite.
Target Market(s)
All targets
Industry/Entity Type
Tourisme
Contact Information for Business Card
adresse, téléphone, email, site internet + réseaux sociaux
Look and feel
Each slider illustrates characteristics of the customer's brand and the style your logo design should communicate.

```html
<!DOCTYPE html>
<html lang="fr">
<head>
<meta charset="utf-8">
<title>Camping Les Brisants-Corail – Carte de visite</title>
<link href="https://fonts.googleapis.com/css2?family=Bebas+Neue&family=Montserrat:wght@500;600;700&family=Dancing+Script:wght@500&display=swap" rel="stylesheet">
<style>
  :root{
    --cream:#f5ecd9;
    --navy:#1f2c46;
    --ocean:#1f6fa8;
    --sky:#8fb3c9;
    --green:#4d7a2e;
    --yellow:#e8a825;
    --orange:#dd6a2a;
    --sand:#d8b97a;
    --ink:#232a3a;
    --rule:#d9b56c;
  }
  *{margin:0;padding:0;box-sizing:border-box}
  html,body{width:890px;height:1200px;overflow:hidden;background:#111}
  body{position:relative;font-family:"Montserrat",sans-serif;color:var(--ink)}
  .card{position:absolute;left:0;width:890px;background:var(--cream);overflow:hidden}
  .card--front{top:0;height:596px}
  .card--back{top:604px;height:596px}

  .brand{position:absolute;display:flex;align-items:center;gap:16px}
  .brand__dot{width:86px;height:86px;border-radius:50%;background:var(--ocean);flex:none}
  .brand__label{font-size:13px;font-weight:600;letter-spacing:4px;color:var(--navy);margin-bottom:4px}
  .brand__name{font-family:"Bebas Neue",sans-serif;font-size:50px;line-height:.92;color:var(--navy)}

  .hook__bold{font-family:"Bebas Neue",sans-serif;font-size:48px;color:var(--green);line-height:1}
  .hook__script{font-family:"Dancing Script",cursive;font-size:36px;color:var(--navy);line-height:1.1}
  .hook__script--green{color:var(--green)}

  .features{position:absolute;left:22px;top:346px;width:420px;display:flex}
  .feature{flex:1;text-align:center;font-size:9.5px;font-weight:600;line-height:1.45;color:var(--navy);border-left:1.5px solid #9c8f74}
  .feature:first-child{border-left:none}
  .feature svg{display:block;margin:0 auto 8px}

  .band{position:absolute;left:0;top:461px;width:476px;height:135px;background:var(--navy);color:#fff;padding:20px 34px}
  .band__title{font-family:"Bebas Neue",sans-serif;font-size:24px;letter-spacing:1.4px;color:var(--cream);padding-left:38px;position:relative}
  .band__title svg{position:absolute;left:0;top:2px}
  .band__addr{font-size:12px;font-weight:500;padding-left:38px;margin-top:2px}
  .band__rule{height:1px;background:#6f7891;margin:14px 0 12px}
  .band__row{display:flex;align-items:center;font-size:13.5px;font-weight:500}
  .band__sep{width:1px;height:26px;background:#8c93a7;margin:0 18px}
  .ico{width:26px;height:26px;border-radius:50%;display:inline-flex;align-items:center;justify-content:center;margin-right:14px;flex:none}

  .scene{position:absolute}
  .seal{position:absolute;border-radius:50%;background:var(--cream);border:2px solid var(--navy)}

  .contacts{position:absolute;left:50px;top:257px;width:346px}
  .contact{display:flex;align-items:center;height:42px}
  .contact__ico{width:42px;height:42px;border-radius:50%;display:flex;align-items:center;justify-content:center;flex:none}
  .contact__text{margin-left:21px;flex:1;font-size:13px;font-weight:600;color:var(--navy);border-bottom:1px solid var(--rule);height:42px;display:flex;align-items:center}
  .contact:last-child .contact__text{border-bottom:none;font-size:12px}
  .contact--addr{height:68px;margin-bottom:4px}
  .contact--addr .contact__text{height:68px;flex-direction:column;align-items:flex-start;justify-content:center;font-size:11px;line-height:1.4}
  .contact--addr .contact__text b{font-size:12px}

  .strip{position:absolute;left:0;top:497px;width:890px;height:99px}
  .strip__labels{position:absolute;left:0;top:497px;width:600px;height:99px;display:flex;color:#fff;font-size:10px;font-weight:500;text-align:center;line-height:1.4}
  .strip__labels div{width:120px;padding-top:12px}
  .strip__labels svg{display:block;margin:0 auto 6px}
  .island{position:absolute;left:600px;top:520px;width:290px;text-align:center;color:var(--cream)}
  .island__name{font-family:"Bebas Neue",sans-serif;font-size:32px;letter-spacing:4px}
  .island__tag{font-size:11.5px;font-weight:600;letter-spacing:1.2px;color:var(--yellow);margin-top:2px}
  .island__rule{width:40px;height:2px;background:var(--yellow);margin:8px auto 0}
</style>
</head>
<body>

<!-- Recto -->
<section class="card card--front">
  <div class="brand" style="left:42px;top:52px">
    <span class="brand__dot"></span>
    <div>
      <div class="brand__label">CAMPING ★★</div>
      <div class="brand__name">LES BRISANTS<br>CORAIL</div>
    </div>
  </div>

  <div style="position:absolute;left:42px;top:228px">
    <div class="hook__bold">RESPIREZ,</div>
    <div class="hook__script">vous êtes arrivés !</div>
    <svg width="120" height="12" style="margin-left:165px;display:block"><path d="M2 9 Q60 -2 118 4" stroke="var(--ocean)" stroke-width="2.5" fill="none"/></svg>
  </div>

  <div class="features">
    <div class="feature">
      <svg width="48" height="48"><circle cx="24" cy="24" r="22" fill="none" stroke="var(--ocean)" stroke-width="1.8"/><circle cx="24" cy="20" r="5" fill="none" stroke="var(--navy)" stroke-width="1.5"/><path d="M12 28q4-3 8 0t8 0 8 0M12 33q4-3 8 0t8 0 8 0" fill="none" stroke="var(--navy)" stroke-width="1.5"/></svg>
      ACCÈS DIRECT<br>AUX PLAGES
    </div>
    <div class="feature">
      <svg width="48" height="48"><circle cx="24" cy="24" r="22" fill="none" stroke="var(--green)" stroke-width="1.8"/><path d="M12 23l12-8 12 8M14 22v11h20V22" fill="none" stroke="var(--navy)" stroke-width="1.5"/></svg>
      MOBIL-HOMES<br>TOUT CONFORT
    </div>
    <div class="feature">
      <svg width="48" height="48"><circle cx="24" cy="24" r="22" fill="none" stroke="var(--yellow)" stroke-width="1.8"/><path d="M13 33l11-19 11 19zM24 14v19" fill="none" stroke="var(--yellow)" stroke-width="1.5"/></svg>
      EMPLACEMENTS<br>SPACIEUX
    </div>
    <div class="feature">
      <svg width="48" height="48"><circle cx="24" cy="24" r="22" fill="none" stroke="var(--orange)" stroke-width="1.8"/><path d="M17 14v20M14 14v5q3 3 6 0v-5M29 14h7q0 8-3.5 8T29 14M32.5 22v12" fill="none" stroke="var(--orange)" stroke-width="1.5"/></svg>
      LE VARECH<br>BAR-RESTAURANT
    </div>
  </div>

  <div class="band">
    <div class="band__title">
      <svg width="22" height="28" viewBox="0 0 22 28"><path d="M11 1C5 1 1 5.5 1 11c0 7 10 16 10 16s10-9 10-16C21 5.5 17 1 11 1z" fill="var(--yellow)"/><circle cx="11" cy="11" r="4" fill="var(--navy)"/></svg>
      THE CORAL BREAKERS - VILLAGES 1 &amp; 2
    </div>
    <div class="band__addr">22 RUE DES MOUETTES, 17310 SAINT-PIERRE-D'OLÉRON</div>
    <div class="band__rule"></div>
    <div class="band__row">
      <span class="ico" style="background:var(--green)"><svg width="14" height="14" viewBox="0 0 24 24"><path d="M6.6 10.8a15 15 0 006.6 6.6l2.2-2.2c.3-.3.7-.4 1-.2 1.1.4 2.3.6 3.6.6.6 0 1 .4 1 1V20c0 .6-.4 1-1 1A17 17 0 013 4c0-.6.4-1 1-1h3.5c.6 0 1 .4 1 1 0 1.3.2 2.5.6 3.6.1.3 0 .7-.2 1z" fill="#fff"/></svg></span>
      +33 5 47 12 38 04
      <span class="band__sep"></span>
      <span class="ico" style="background:var(--yellow)"><svg width="15" height="15" viewBox="0 0 24 24" fill="none" stroke="#fff" stroke-width="1.8"><circle cx="12" cy="12" r="9"/><path d="M3 12h18M12 3c3 3 3 15 0 18M12 3c-3 3-3 15 0 18"/></svg></span>
      www.lesbrisants-corail.fr
    </div>
  </div>

  <div class="scene" role="img" aria-label="Illustration : phare blanc sur la dune, soleil orange, mouettes, océan et sentier de sable bordé d'oyats"
       style="left:0;top:0;width:890px;height:596px;clip-path:polygon(472px 0,890px 0,890px 596px,476px 596px,476px 340px,580px 340px);background:linear-gradient(160deg,#1f4e82 0%,#6f9ab8 35%,#5d8a4a 62%,#c9a567 100%)"></div>
  <div class="seal" role="img" aria-label="Cachet décoratif" style="left:720px;top:427px;width:140px;height:140px"></div>
</section>

<!-- Verso -->
<section class="card card--back">
  <div class="scene" role="img" aria-label="Carte illustrée de l'Île d'Oléron avec Saint-Denis et Saint-Pierre, voilier, phare et maison de plage"
       style="left:405px;top:0;width:485px;height:500px;background:linear-gradient(120deg,#9dc0d8 0%,#c9dbe0 45%,#e9e1c9 70%,#6f8f4e 100%)"></div>
  <div class="seal" role="img" aria-label="Cachet décoratif" style="left:708px;top:33px;width:132px;height:132px"></div>

  <div class="brand" style="left:48px;top:40px">
    <span class="brand__dot"></span>
    <div>
      <div class="brand__label">CAMPING ★★</div>
      <div class="brand__name">LES BRISANTS<br>CORAIL</div>
    </div>
  </div>

  <div style="position:absolute;left:52px;top:172px">
    <div class="hook__script hook__script--green">Respirez,</div>
    <div class="hook__script">vous êtes arrivés !</div>
    <svg width="110" height="12" style="margin-left:130px;display:block"><path d="M2 9 Q55 -2 108 4" stroke="var(--ocean)" stroke-width="2.5" fill="none"/></svg>
  </div>

  <div class="contacts">
    <div class="contact contact--addr">
      <span class="contact__ico" style="background:var(--ocean)"><svg width="18" height="22" viewBox="0 0 22 28"><path d="M11 1C5 1 1 5.5 1 11c0 7 10 16 10 16s10-9 10-16C21 5.5 17 1 11 1z" fill="#fff"/><circle cx="11" cy="11" r="4" fill="var(--ocean)"/></svg></span>
      <div class="contact__text"><b>THE CORAL BREAKERS - VILLAGES 1 &amp; 2</b>22 RUE DES MOUETTES<br>17310 SAINT-PIERRE-D'OLÉRON, FRANCE</div>
    </div>
    <div class="contact">
      <span class="contact__ico" style="background:var(--green)"><svg width="18" height="18" viewBox="0 0 24 24"><path d="M6.6 10.8a15 15 0 006.6 6.6l2.2-2.2c.3-.3.7-.4 1-.2 1.1.4 2.3.6 3.6.6.6 0 1 .4 1 1V20c0 .6-.4 1-1 1A17 17 0 013 4c0-.6.4-1 1-1h3.5c.6 0 1 .4 1 1 0 1.3.2 2.5.6 3.6.1.3 0 .7-.2 1z" fill="#fff"/></svg></span>
      <div class="contact__text">+33 5 47 12 38 04</div>
    </div>
    <div class="contact">
      <span class="contact__ico" style="background:var(--yellow)"><svg width="20" height="16" viewBox="0 0 20 16" fill="none" stroke="#fff" stroke-width="1.6"><rect x="1" y="1" width="18" height="14" rx="1"/><path d="M1 2l9 7 9-7"/></svg></span>
      <div class="contact__text">info@lesbrisants-corail.fr</div>
    </div>
    <div class="contact">
      <span class="contact__ico" style="background:var(--orange)"><svg width="20" height="20" viewBox="0 0 24 24" fill="none" stroke="#fff" stroke-width="1.6"><circle cx="12" cy="12" r="9"/><path d="M3 12h18M12 3c3 3 3 15 0 18M12 3c-3 3-3 15 0 18"/></svg></span>
      <div class="contact__text">www.lesbrisants-corail.fr</div>
    </div>
    <div class="contact">
      <span class="contact__ico" style="background:#5a3f6e"></span>
      <div class="contact__text" style="font-weight:500">SUIVEZ-NOUS<span style="width:1px;height:20px;background:var(--navy);margin:0 12px"></span><b style="font-weight:600">@lesbrisantscorail</b></div>
    </div>
  </div>

  <svg class="strip" width="890" height="99" viewBox="0 0 890 99">
    <rect width="890" height="99" fill="var(--navy)"/>
    <polygon points="0,0 140,0 124,99 0,99" fill="var(--ocean)"/>
    <polygon points="140,0 270,0 254,99 124,99" fill="var(--green)"/>
    <polygon points="270,0 390,0 374,99 254,99" fill="var(--yellow)"/>
    <polygon points="390,0 600,0 580,99 374,99" fill="var(--orange)"/>
    <path d="M600 0 Q690 -8 890 -30 V0z" fill="var(--navy)"/>
  </svg>
  <div class="strip__labels">
    <div><svg width="36" height="30"><circle cx="18" cy="11" r="5" fill="none" stroke="#fff" stroke-width="1.4"/><path d="M4 20q4-3 7 0t7 0 7 0 7 0M4 26q4-3 7 0t7 0 7 0 7 0" fill="none" stroke="#fff" stroke-width="1.4"/></svg>ACCÈS DIRECT<br>AUX PLAGES</div>
    <div style="margin-left:4px"><svg width="36" height="30"><path d="M4 13l14-10 14 10M7 12v15h22V12" fill="none" stroke="#fff" stroke-width="1.4"/></svg>MOBIL-HOMES<br>TOUT CONFORT</div>
    <div style="margin-left:4px"><svg width="36" height="30"><path d="M5 28l13-24 13 24zM18 4v24" fill="none" stroke="#fff" stroke-width="1.4"/></svg>EMPLACEMENTS<br>SPACIEUX</div>
    <div style="width:170px;margin-left:8px"><svg width="36" height="30"><path d="M10 3v25M7 3v6q3 3 6 0V3M22 3h8q0 10-4 10T22 3M26 13v15" fill="none" stroke="#fff" stroke-width="1.4"/></svg>LE VARECH<br>BAR-RESTAURANT</div>
  </div>
  <div class="island">
    <div class="island__name">ÎLE D'OLÉRON</div>
    <div class="island__tag">NATURE • OCÉAN • CONVIVIALITÉ</div>
    <div class="island__rule"></div>
  </div>
</section>

</body>
</html>
```